Business Card Design Project - The Bridgeway Partners

Company Name - The Bridgeway Partners

We need a unique logo and business cards

We are a team of experienced IT professionals who specialize in providing business value to organizations via the analysis and understanding the challenges of your particular organization. We focus on understanding the challenges first, and execute against your priorities partnering with your highly valued key resources.

Our extensive experience and focus on Agile delivery methodologies help our clients continuously improve and deliver quality solutions. Using this approach we will always deliver the greatest return on your investments.

Target Market(s)

Large organizations IT departments

Industry/Entity Type

Business

Font styles to use
Serif
Sans Serif

Requirements
Should not have
• no pictures

```html
<!DOCTYPE html>
<html lang="en">
<head>
<meta charset="utf-8">
<title>The Bridgeway Partners – Business Cards</title>
<link href="https://fonts.googleapis.com/css2?family=Aldrich&display=swap" rel="stylesheet">
<style>
  :root {
    --backdrop: #6a6a6a;
    --card-white: #ffffff;
    --card-grey: #e4e5e7;
    --brand-navy: #1d3f8f;
    --brand-blue: #1a73c9;
    --brand-bright: #1fa3e8;
    --ink-dark: #2b2b2b;
    --ink-mid: #444;
    --rule-dark: #2d2f33;
  }
  * { margin: 0; padding: 0; box-sizing: border-box; }
  html, body { width: 1200px; height: 750px; overflow: hidden; }
  body {
    background: var(--backdrop);
    font-family: "Aldrich", sans-serif;
    display: flex;
    align-items: center;
    justify-content: center;
    gap: 40px;
  }
  .card {
    position: relative;
    width: 540px;
    height: 309px;
    overflow: hidden;
    background: linear-gradient(135deg, var(--card-white) 0%, var(--card-grey) 100%);
    box-shadow: 0 6px 18px rgba(0,0,0,.35);
  }
  .card-art { position: absolute; inset: 0; width: 100%; height: 100%; }

  /* Brand lockup */
  .brand { display: flex; align-items: center; gap: 8px; }
  .brand-dot { width: 14px; height: 14px; border-radius: 50%; background: var(--brand-navy); flex: none; }
  .brand-name { color: var(--brand-navy); font-size: 22px; letter-spacing: .5px; white-space: nowrap; }

  /* Front */
  .card-front .brand { position: absolute; top: 78px; left: 0; right: 0; justify-content: center; }
  .front-url { font-family: "Aldrich", sans-serif; font-size: 15px; fill: #fff; letter-spacing: .5px; }

  /* Back */
  .card-back .brand { position: absolute; top: 98px; left: 38px; gap: 7px; }
  .card-back .brand-dot { width: 12px; height: 12px; }
  .card-back .brand-name { font-size: 17px; letter-spacing: .3px; }
  .holder { position: absolute; top: 146px; left: 38px; }
  .holder-marker { position: absolute; left: -38px; top: 4px; width: 14px; height: 28px; background: var(--brand-blue); }
  .holder-name { font-size: 16px; color: var(--ink-dark); letter-spacing: 1px; text-transform: uppercase; }
  .holder-title { font-size: 11.5px; color: var(--ink-mid); margin-top: 2px; }

  .contact { position: absolute; top: 56px; right: 20px; text-align: right; color: #fff; font-size: 11px; line-height: 1.35; font-style: normal; }
  .contact-address { margin-bottom: 14px; }
  .contact-line { display: flex; align-items: center; justify-content: flex-end; gap: 7px; height: 21px; white-space: nowrap; }
  .contact-icon { width: 12px; height: 12px; flex: none; }
</style>
</head>
<body>

<section class="card card-front" aria-label="Business card front">
  <svg class="card-art" viewBox="0 0 540 309">
    <defs>
      <linearGradient id="bandFill" x1="0" x2="1" y1="0" y2="0">
        <stop offset="0" stop-color="#2848a8"/>
        <stop offset=".55" stop-color="#1e8fe0"/>
        <stop offset="1" stop-color="#1a5fc2"/>
      </linearGradient>
    </defs>
    <path d="M0,232 Q270,168 540,140" fill="none" stroke="var(--rule-dark)" stroke-width="4"/>
    <path d="M0,238 Q270,174 540,146 L540,190 Q270,214 0,282 Z" fill="url(#bandFill)"/>
    <text class="front-url" x="270" y="224" text-anchor="middle" transform="rotate(-7 270 215)">www.bridgewaypartners.com</text>
  </svg>
  <div class="brand">
    <span class="brand-dot"></span>
    <span class="brand-name">The Bridgeway Partners</span>
  </div>
</section>

<section class="card card-back" aria-label="Business card back">
  <svg class="card-art" viewBox="0 0 540 309">
    <defs>
      <radialGradient id="discFill" cx=".3" cy=".45" r=".7">
        <stop offset="0" stop-color="var(--brand-bright)"/>
        <stop offset="1" stop-color="#1556b8"/>
      </radialGradient>
    </defs>
    <circle cx="620" cy="150" r="340" fill="none" stroke="var(--brand-blue)" stroke-width="2.5"/>
    <circle cx="620" cy="150" r="330" fill="url(#discFill)"/>
  </svg>

  <div class="brand">
    <span class="brand-dot"></span>
    <span class="brand-name">The Bridgeway Partners</span>
  </div>

  <div class="holder">
    <span class="holder-marker"></span>
    <p class="holder-name">Daniel Hartwell</p>
    <p class="holder-title">Managing Director</p>
  </div>

  <address class="contact">
    <p class="contact-address">214, 9th floor,<br>Harbor Point Road NWK</p>
    <p class="contact-line">012 555 0148
      <svg class="contact-icon" viewBox="0 0 12 12" aria-label="Phone"><path d="M2 1l2 0 1 3-1.4 1a7 7 0 0 0 3.4 3.4L8 7l3 1v2a1 1 0 0 1-1 1A9 9 0 0 1 1 2a1 1 0 0 1 1-1z" fill="#fff"/></svg>
    </p>
    <p class="contact-line">012 555 0149
      <svg class="contact-icon" viewBox="0 0 12 12" aria-label="Mobile"><rect x="3" y="0.5" width="6" height="11" rx="1" fill="none" stroke="#fff"/><circle cx="6" cy="9.6" r=".7" fill="#fff"/></svg>
    </p>
    <p class="contact-line">012 555 0150
      <svg class="contact-icon" viewBox="0 0 12 12" aria-label="Fax"><rect x="3" y="1" width="6" height="4" fill="#fff"/><rect x="1" y="5" width="10" height="6" rx="1" fill="#fff"/></svg>
    </p>
    <p class="contact-line">dhartwell@bridgeway.com
      <svg class="contact-icon" viewBox="0 0 12 12" aria-label="Email"><rect x="0.5" y="2.5" width="11" height="7" fill="#fff"/><path d="M0.5 2.5l5.5 4 5.5-4" fill="none" stroke="#1a73c9"/></svg>
    </p>
    <p class="contact-line">www.bridgewaypartners.com
      <svg class="contact-icon" viewBox="0 0 12 12" aria-label="Website"><circle cx="6" cy="6" r="5.2" fill="none" stroke="#fff"/><ellipse cx="6" cy="6" rx="2.2" ry="5.2" fill="none" stroke="#fff"/><path d="M1 6h10" stroke="#fff"/></svg>
    </p>
  </address>
</section>

</body>
</html>
```